Corvalen Capital Modern Business Card

We need a modern business card template designed for Corvalen Capital.
Corvalen Capital is a diversified global cryptocurrency investment fund.

The font under the logo: Hiragino Kaku Gothic Pro

Color Hexcode: Main colors white (ffffff) & teal (188383), we are open to adding #fcca46 as an accent

Need time to get feedback from my team and to make sure designers better understand the brief.

Target Market(s)

Accredited Investors, high net worth individuals and institutional investors

Industry/Entity Type

Investment

Contact Information for Business Card

Contact Information should contain
Name
main phone +1 720 555 0147
cell
email

Font styles to use
Sans Serif
Other font styles liked:
• Hiragino Kaku Gothic Pro

Requirements
Must have
• would like to have icons that identify the contact information
• include our website: www.corvalencapital.example
• include our Tagline: Diversified Crypto Investment Funds
Nice to have
• Would like to have a simple back side with the logo (without the words) and plenty of space

```html
<!DOCTYPE html>
<html lang="en">
<head>
<meta charset="UTF-8">
<title>Corvalen Capital Business Card</title>
<link href="https://fonts.googleapis.com/css2?family=Oswald:wght@500&family=Work+Sans:wght@400;500&display=swap" rel="stylesheet">
<style>
  :root {
    --stage: #1b1b1b;
    --card: #262626;
    --card-edge: #2e2e2e;
    --teal: #1f9d9d;
    --white: #ffffff;
    --mark-grey: #b9bcbd;
  }
  * { margin: 0; padding: 0; box-sizing: border-box; }
  html, body {
    width: 1200px;
    height: 900px;
    overflow: hidden;
    background: var(--stage);
  }
  .stage {
    position: relative;
    width: 1200px;
    height: 900px;
  }
  .card {
    position: absolute;
    left: 250px;
    width: 700px;
    height: 400px;
    overflow: hidden;
    background: linear-gradient(135deg, var(--card) 0%, #2b2b2b 60%, var(--card-edge) 100%);
    box-shadow: 0 14px 30px rgba(0, 0, 0, 0.55);
  }
  .card--logo { top: 40px; }
  .card--contact { top: 470px; }

  .brand-block {
    position: absolute;
    left: 0;
    right: 0;
    top: 170px;
    text-align: center;
  }
  .brand-block__name {
    font-family: "Work Sans", sans-serif;
    font-weight: 400;
    font-size: 34px;
    letter-spacing: 2px;
    color: var(--mark-grey);
    text-transform: uppercase;
  }
  .brand-block__tagline {
    margin-top: 10px;
    font-family: "Work Sans", sans-serif;
    font-weight: 400;
    font-size: 14px;
    letter-spacing: 2.4px;
    color: var(--teal);
    text-transform: uppercase;
  }

  .identity {
    position: absolute;
    right: 375px;
    top: 120px;
    text-align: right;
  }
  .identity__name {
    font-family: "Oswald", sans-serif;
    font-weight: 500;
    font-size: 40px;
    letter-spacing: 1.5px;
    line-height: 1.1;
    color: var(--teal);
    text-transform: uppercase;
  }
  .identity__role {
    font-family: "Work Sans", sans-serif;
    font-size: 18px;
    letter-spacing: 0.8px;
    color: var(--white);
    margin-top: 2px;
  }
  .divider {
    position: absolute;
    left: 345px;
    top: 124px;
    width: 2px;
    height: 94px;
    background: var(--teal);
  }
  .contact-list {
    position: absolute;
    left: 367px;
    top: 124px;
    list-style: none;
  }
  .contact-list li {
    display: flex;
    align-items: center;
    gap: 12px;
    height: 24px;
    font-family: "Work Sans", sans-serif;
    font-size: 16px;
    letter-spacing: 0.4px;
    color: var(--white);
    white-space: nowrap;
  }
  .contact-list svg {
    width: 16px;
    height: 16px;
    flex: none;
  }
  .address {
    position: absolute;
    left: 70px;
    top: 318px;
    font-family: "Work Sans", sans-serif;
    font-size: 18px;
    letter-spacing: 0.8px;
    color: var(--white);
    white-space: nowrap;
  }
  .address__company {
    font-family: "Oswald", sans-serif;
    font-weight: 500;
    font-size: 19px;
    letter-spacing: 1px;
    color: var(--teal);
    text-transform: uppercase;
  }
</style>
</head>
<body>
<main class="stage">
  <section class="card card--logo" aria-label="Card back">
    <div class="brand-block">
      <p class="brand-block__name">Corvalen Capital</p>
      <p class="brand-block__tagline">Diversified Crypto Investment Funds</p>
    </div>
  </section>

  <section class="card card--contact" aria-label="Card front">
    <div class="identity">
      <h1 class="identity__name">Daniel Harrow</h1>
      <p class="identity__role">Managing Director</p>
    </div>
    <span class="divider"></span>
    <ul class="contact-list">
      <li>
        <svg viewBox="0 0 16 16" aria-hidden="true"><path fill="var(--teal)" d="M3.6 1.5l2.2 2.6-1.3 1.6c.9 2 2.4 3.5 4.4 4.4l1.6-1.3 2.6 2.2-1.2 2.3C7.2 14.7 1.3 8.8 1.3 3z"/></svg>
        <span>+1 720 555 0147</span>
      </li>
      <li>
        <svg viewBox="0 0 16 16" aria-hidden="true"><rect x="1.5" y="3.5" width="13" height="9" fill="var(--teal)"/><path d="M1.5 3.5L8 9l6.5-5.5" fill="none" stroke="var(--card)" stroke-width="1.2"/></svg>
        <span>info@corvalencapital.example</span>
      </li>
      <li>
        <svg viewBox="0 0 16 16" aria-hidden="true"><g fill="none" stroke="var(--teal)" stroke-width="1.3"><circle cx="8" cy="8" r="6.3"/><ellipse cx="8" cy="8" rx="2.8" ry="6.3"/><path d="M1.8 8h12.4M2.8 4.8h10.4M2.8 11.2h10.4"/></g></svg>
        <span>www.corvalencapital.example</span>
      </li>
    </ul>
    <p class="address"><span class="address__company">Corvalen Capital :</span> 1087 Eastbrook, Halden str. 24/C, Norway</p>
  </section>
</main>
</body>
</html>
```